BrightKeel Business Card Contest

We are looking for a modern business card that catches attention and is unique. Attached is the brand guide and logo files. Please note that the back side (not the side with our name and info) with be UV raise printed, so have fun with the design there. We want to include Name, Title, Phone number, email, website.

Contact Information for Business Card

Please see project description

```html
<!DOCTYPE html>
<html lang="en">
<head>
<meta charset="utf-8">
<title>BrightKeel Business Card</title>
<link rel="stylesheet" href="https://fonts.googleapis.com/css2?family=Poppins:wght@400;500;600;700&display=swap">
<style>
  :root {
    --stage: #3a3a3a;
    --card: #141414;
    --card-edge: #e0261f;
    --ink-light: #ffffff;
    --ink-soft: #e6e6e6;
    --accent: #e0261f;
    --panel-light: #d9d9d9;
    --panel-dark: #050505;
  }
  * { box-sizing: border-box; margin: 0; padding: 0; }
  html, body {
    width: 1200px;
    height: 875px;
    overflow: hidden;
  }
  body {
    background: var(--stage);
    font-family: "Poppins", sans-serif;
    position: relative;
  }
  .card {
    position: absolute;
    top: 288px;
    width: 520px;
    height: 300px;
    background: var(--card);
    border-radius: 22px;
    border-bottom: 4px solid var(--card-edge);
    border-left: 2px solid var(--card-edge);
    overflow: hidden;
    box-shadow: 0 24px 50px rgba(0,0,0,0.45);
  }
  .card--back { left: 50px; }
  .card--front { left: 630px; }

  /* Back side: raised UV artwork area */
  .uv-artwork {
    position: absolute;
    left: 0;
    top: 60px;
    width: 290px;
    height: 200px;
    background: linear-gradient(100deg, var(--panel-light) 0%, #8a8a8a 35%, #1c1c1c 60%, var(--panel-dark) 100%);
    clip-path: polygon(0 0, 78% 0, 100% 50%, 78% 100%, 0 100%);
  }
  .back-wordmark {
    position: absolute;
    right: 34px;
    bottom: 48px;
    color: var(--ink-light);
    font-size: 46px;
    font-weight: 500;
    letter-spacing: 0.5px;
  }

  /* Front side */
  .holder {
    position: absolute;
    right: 34px;
    top: 40px;
    text-align: right;
  }
  .holder__name {
    color: var(--accent);
    font-size: 26px;
    font-weight: 700;
    line-height: 1.1;
  }
  .holder__title {
    color: var(--ink-soft);
    font-size: 14px;
    font-weight: 400;
    margin-top: 4px;
  }
  .brand {
    position: absolute;
    left: 36px;
    top: 60px;
    display: flex;
    align-items: center;
    gap: 12px;
  }
  .brand__mark {
    width: 14px;
    height: 14px;
    background: var(--accent);
  }
  .brand__name {
    color: var(--ink-light);
    font-size: 40px;
    font-weight: 500;
    letter-spacing: 0.5px;
  }
  .address {
    position: absolute;
    left: 40px;
    top: 140px;
    color: var(--ink-soft);
    font-size: 13px;
    line-height: 1.5;
  }
  .contacts {
    position: absolute;
    left: 40px;
    top: 194px;
    list-style: none;
    color: var(--ink-soft);
    font-size: 13px;
    line-height: 1.6;
  }
  .contacts li {
    display: flex;
    align-items: center;
    gap: 9px;
  }
  .contacts svg {
    width: 13px;
    height: 13px;
    flex: none;
  }
</style>
</head>
<body>

  <section class="card card--back" aria-label="Business card, back side">
    <div class="uv-artwork" role="img" aria-label="Raised UV geometric artwork in grey to black tones"></div>
    <div class="back-wordmark">BrightKeel</div>
  </section>

  <section class="card card--front" aria-label="Business card, front side">
    <div class="holder">
      <div class="holder__name">Erik Halvorsen</div>
      <div class="holder__title">Managing Director</div>
    </div>

    <div class="brand">
      <span class="brand__mark"></span>
      <span class="brand__name">BrightKeel</span>
    </div>

    <address class="address" style="font-style:normal">
      P.O. Box 2740<br>
      Fairhaven, WA 98225
    </address>

    <ul class="contacts">
      <li>
        <svg viewBox="0 0 16 16" aria-hidden="true"><path fill="#e0261f" d="M3.6 1.5l2.3 2.7-1.3 1.6c.9 2 2.6 3.7 4.6 4.6l1.6-1.3 2.7 2.3-1.4 2.1C6.9 13.2 2.8 9.1 1.5 3z"/></svg>
        555 214 309
      </li>
      <li>
        <svg viewBox="0 0 16 16" aria-hidden="true"><rect x="1" y="3" width="14" height="10" fill="#e0261f"/><path d="M1 3.5l7 5 7-5" fill="none" stroke="#141414" stroke-width="1.4"/></svg>
        info@brightkeel.com
      </li>
      <li>
        <svg viewBox="0 0 16 16" aria-hidden="true"><circle cx="8" cy="8" r="6.5" fill="none" stroke="#e0261f" stroke-width="1.5"/><ellipse cx="8" cy="8" rx="2.8" ry="6.5" fill="none" stroke="#e0261f" stroke-width="1.2"/><path d="M1.5 8h13" stroke="#e0261f" stroke-width="1.2"/></svg>
        www.brightkeel.com
      </li>
    </ul>
  </section>

</body>
</html>
```